Post announcing a new website

Please prepare a poster to announce Harbourline Tavern's new website and Marlo's Asian Kitchen online ordering system.

The poster (A3) should have space in the bottom third for text in multiple languages.

Please use www.harbourlinetavern.com.au as a guide to style

Thanks all, I have sent these designs to the client and will get back to you shortly.

```html
<!DOCTYPE html>
<html lang="en">
<head>
<meta charset="utf-8">
<title>Harbourline Tavern – New Website Poster</title>
<link rel="stylesheet" href="https://fonts.googleapis.com/css2?family=Luckiest+Guy&family=Bangers&family=Mystery+Quest&family=Open+Sans:wght@300;400;700&display=swap">
<style>
  :root {
    --backdrop: #1a1a1a;
    --crimson: #a51d35;
    --crimson-deep: #8e1529;
    --ray: rgba(255,255,255,0.06);
    --band-dark: #231815;
    --sun-yellow: #f8e34c;
    --sun-orange: #f2951c;
    --accent-orange: #f39a1e;
    --ink: #2a1a12;
    --white: #ffffff;
    --ornament: #c9566a;
  }
  * { box-sizing: border-box; margin: 0; padding: 0; }
  html, body { width: 1200px; height: 800px; overflow: hidden; }
  body {
    background: var(--backdrop);
    font-family: "Open Sans", Arial, sans-serif;
    position: relative;
  }
  .poster {
    position: absolute;
    left: 338px; top: 30px;
    width: 524px; height: 740px;
    overflow: hidden;
    background: linear-gradient(180deg, var(--sun-yellow) 0%, var(--sun-orange) 100%);
  }
  .poster__hero {
    position: absolute; inset: 0 0 auto 0; height: 385px;
    background: var(--crimson);
    overflow: hidden;
  }
  .poster__rays { position: absolute; inset: 0; width: 100%; height: 100%; }
  .ornament {
    position: absolute;
    background: radial-gradient(ellipse at center, var(--ornament) 0%, rgba(165,29,53,0) 70%);
    opacity: 0.8;
  }
  .ornament--phoenix { left: 8px; top: 70px; width: 140px; height: 170px; }
  .ornament--dragon { right: 14px; top: 18px; width: 140px; height: 120px; }
  .kitchen-title {
    position: absolute; top: 62px; left: 0; right: 0;
    text-align: center;
    font-family: "Mystery Quest", cursive;
    font-weight: 400;
    color: var(--white);
    font-size: 30px; line-height: 32px;
    letter-spacing: 1px;
    text-transform: uppercase;
  }
  .venue-name {
    position: absolute; top: 150px; left: 0; right: 0;
    display: flex; justify-content: center; align-items: center; gap: 8px;
    font-weight: 700; font-size: 17px;
    color: var(--accent-orange);
  }
  .venue-name__dot {
    width: 22px; height: 22px; border-radius: 50%;
    background: var(--accent-orange);
  }
  .headline {
    position: absolute; top: 196px; left: 0; right: 0;
    text-align: center;
    font-family: "Luckiest Guy", "Bangers", Impact, sans-serif;
    font-weight: 400;
    color: var(--white);
  }
  .headline__lead { display: block; font-size: 62px; line-height: 66px; }
  .headline__venue { display: block; font-size: 31px; line-height: 36px; }
  .headline__tail { display: block; font-size: 54px; line-height: 58px; }
  .info-band {
    position: absolute; top: 385px; left: 0; right: 0; height: 68px;
    background: var(--band-dark);
    color: var(--white);
    text-align: center;
    padding-top: 9px;
    font-size: 12px; line-height: 17px;
  }
  .info-band__title { font-weight: 700; font-size: 13px; }
  .language-space {
    position: absolute; top: 478px; left: 0; right: 0;
    text-align: center;
    font-weight: 300; font-size: 31px;
    color: var(--ink);
  }
  .poster__footer-shape { position: absolute; left: 0; bottom: 0; width: 524px; height: 200px; }
  .footer-seal {
    position: absolute; left: 196px; top: 552px;
    width: 156px; height: 156px; border-radius: 50%;
    background: radial-gradient(circle, var(--sun-yellow) 0%, var(--sun-orange) 100%);
    border: 5px solid var(--crimson-deep);
    display: flex; align-items: center; justify-content: center;
    text-align: center;
    font-weight: 700; font-size: 16px; line-height: 20px;
    color: var(--crimson);
  }
  .contact {
    position: absolute; right: 12px; top: 584px;
    width: 150px;
    text-align: right;
    font-weight: 700; font-size: 9.5px; line-height: 15px;
    color: var(--accent-orange);
  }
  .contact__phone { text-transform: uppercase; }
  .address {
    position: absolute; left: 20px; top: 668px;
    font-weight: 700; font-size: 10px; line-height: 15px;
    color: var(--accent-orange);
    text-transform: uppercase;
  }
</style>
</head>
<body>
  <article class="poster">
    <section class="poster__hero">
      <svg class="poster__rays" viewBox="0 0 524 385" aria-hidden="true">
        <g fill="var(--ray)">
          <polygon points="262,330 -200,-100 -60,-200"/>
          <polygon points="262,330 40,-200 160,-200"/>
          <polygon points="262,330 230,-200 300,-200"/>
          <polygon points="262,330 370,-200 480,-200"/>
          <polygon points="262,330 580,-200 724,-100"/>
          <polygon points="262,330 724,60 724,200"/>
          <polygon points="262,330 -200,60 -200,200"/>
          <polygon points="262,330 724,330 724,420"/>
          <polygon points="262,330 -200,330 -200,420"/>
        </g>
      </svg>
      <div class="ornament ornament--phoenix" role="img" aria-label="Line illustration of a phoenix"></div>
      <div class="ornament ornament--dragon" role="img" aria-label="Line illustration of a dragon"></div>
      <h2 class="kitchen-title">Marlo's Asian<br>Kitchen</h2>
      <div class="venue-name"><span>Harbourline Tavern</span><span class="venue-name__dot"></span></div>
      <h1 class="headline">
        <span class="headline__lead">Visit New !</span>
        <span class="headline__venue">Harbourline Tavern</span>
        <span class="headline__tail">Website!</span>
      </h1>
    </section>

    <section class="info-band">
      <p class="info-band__title">Harbourline Tavern &amp; Restaurant.</p>
      <p>5 Star Scores on Clean Plate Rating, great food, clean kitchen<br>and fresh ingredients. Quality Asian food located in the inner city.</p>
    </section>

    <p class="language-space">Other language text place</p>

    <svg class="poster__footer-shape" viewBox="0 0 524 200" aria-hidden="true">
      <path fill="var(--crimson)" d="M0,200 V80
        h10 v-12 a6,6 0 0 1 6,-6 h16 a6,6 0 0 1 6,6 v12
        h20 v-12 a6,6 0 0 1 6,-6 h16 a6,6 0 0 1 6,6 v12
        h20 v-12 a6,6 0 0 1 6,-6 h16 a6,6 0 0 1 6,6 v12
        h20 v-12 a6,6 0 0 1 6,-6 h16 a6,6 0 0 1 6,6 v12
        H272 V30
        h158 v-10 a6,6 0 0 1 6,-6 h14 a6,6 0 0 1 6,6 v10
        h16 v-10 a6,6 0 0 1 6,-6 h14 a6,6 0 0 1 6,6 v10
        H524 V200 Z"/>
    </svg>
    <div class="footer-seal">Harbourline<br>Tavern</div>
    <div class="contact"><span class="contact__phone">Call: 123-456-789</span><br>www.harbourlinetavern.com.au</div>
    <div class="address">Address line 1<br>Street 1, Pin-0000</div>
  </article>
</body>
</html>
```